HR Technology Company (Corvixo) needs a consistent powerpoint deck for future presentations

We are Corvixo (corvixo-example.com). You can visit our website for colours scheme etc. I am looking for a full PPT pack which can be used for various presentations in the future. Sales Presentation, Company Overview etc. This must include charts, graphs, services (4/6/8 items), people slide, timeline slides etc among all the other common slides.

```html
<!DOCTYPE html>
<html lang="en">
<head>
<meta charset="utf-8">
<title>Corvixo Presentation Deck</title>
<link rel="stylesheet" href="https://fonts.googleapis.com/css2?family=Montserrat:wght@500;600;700;800&family=Roboto:wght@400;500;700&display=swap">
<style>
:root{
  --orange:#ee7623;
  --orange-soft:#f7b887;
  --navy:#1b2c4f;
  --ink:#111111;
  --grey-text:#555b66;
  --canvas:#dcdcdc;
  --sheet:#ffffff;
  --swoosh:#f1f1f1;
  --grid:#e3e3e3;
}
*{box-sizing:border-box;margin:0;padding:0}
html,body{width:1200px;height:4129px;overflow:hidden;background:var(--canvas)}
body{position:relative;font-family:"Roboto",Arial,sans-serif;color:var(--navy)}
.slide{position:absolute;left:51px;width:1096px;height:617px;background:var(--sheet);overflow:hidden}
.slide > *{position:absolute}
.swoosh{left:0;top:0;width:1096px;height:617px}
.title-tab{left:0;top:30px;width:30px;height:28px;background:var(--orange);border-radius:0 14px 14px 0}
.slide-title{left:58px;top:26px;font-family:"Montserrat",sans-serif;font-weight:700;font-size:35px;letter-spacing:.3px;color:var(--navy);line-height:1.2}
.brand{right:42px;top:32px;display:flex;align-items:center;gap:8px;font-family:"Montserrat",sans-serif;font-weight:700;font-size:22px;color:var(--navy)}
.brand-mark{width:14px;height:14px;background:var(--orange)}
.page-no{right:18px;bottom:14px;width:26px;height:26px;border-radius:50%;background:var(--ink);color:#fff;font-size:11px;font-weight:700;display:flex;align-items:center;justify-content:center}
.footer{left:54px;top:565px;display:flex;align-items:center;gap:6px;font-size:8px;color:var(--ink)}
.social{width:22px;height:22px;border:1.3px solid var(--ink);border-radius:50%}
.footer .divider{width:1px;height:22px;background:#999;margin:0 10px 0 8px}

/* cover */
.cover-photo{left:0;top:0;width:1096px;height:617px;background:linear-gradient(100deg,#1f2c3e 0%,#3b4a5c 38%,#8a6b44 70%,#c8954f 100%)}
.cover-band{left:426px;top:375px;width:626px;height:202px;background:var(--orange);color:#fff;text-align:right;padding:26px 36px 0 0;font-family:"Montserrat",sans-serif}
.cover-band .kicker{font-size:35px;font-weight:700;letter-spacing:.5px}
.cover-band .name{font-size:88px;font-weight:800;line-height:1.05;letter-spacing:1px}

/* timeline */
.milestone{width:220px;text-align:center;transform:translateX(-50%)}
.milestone .year{font-family:"Montserrat",sans-serif;font-weight:700;font-size:22px;color:var(--ink);margin-bottom:10px}
.milestone p{font-size:13.5px;line-height:22px;color:var(--grey-text)}

/* services */
.service{width:380px}
.service h3{font-family:"Montserrat",sans-serif;font-weight:600;font-size:20px;color:var(--navy);margin-bottom:8px}
.service p{font-size:11px;font-weight:700;line-height:25px;color:var(--ink)}
.service-tag{width:100px;height:64px}

/* features */
.feature{left:711px;width:330px}
.feature h4{font-family:"Montserrat",sans-serif;font-weight:600;font-size:18px;color:var(--navy);padding-left:24px;position:relative;margin-bottom:6px}
.feature h4::before{content:"";position:absolute;left:0;top:5px;width:11px;height:11px;border-radius:50%;background:var(--orange)}
.feature p{font-size:12.5px;line-height:20px;color:var(--grey-text);padding-left:24px}

/* team */
.member{width:240px;text-align:center;transform:translateX(-50%)}
.portrait{width:150px;height:150px;border-radius:50%;background:linear-gradient(160deg,#e6e6e6,#9aa2ab);margin:0 auto 14px}
.member h5{font-family:"Montserrat",sans-serif;font-weight:700;font-size:15px;color:var(--navy)}
.member .role{font-size:12px;color:#777;margin:3px 0 8px}
.member p{font-size:12px;line-height:20px;color:var(--grey-text)}

/* thank you */
.thanks-band{left:0;top:0;width:1096px;height:83px;background:var(--swoosh)}
.thanks-title{left:43px;top:12px;font-family:"Montserrat",sans-serif;font-weight:800;font-size:46px;color:var(--navy)}
.thanks-photo{left:0;top:83px;width:1096px;height:457px;background:linear-gradient(120deg,#4d5d66 0%,#9fb3b8 45%,#d8dfdc 70%,#6f7c80 100%)}
</style>
</head>
<body>

<!-- Slide 1: Cover -->
<section class="slide" style="top:45px">
  <div class="cover-photo" role="img" aria-label="Photo of a business executive in a suit and glasses against a city at dusk"></div>
  <svg class="swoosh" viewBox="0 0 1096 617" aria-hidden="true"><path d="M590 0 C 800 40, 980 150, 1096 304 L1096 0 Z" fill="#f1f1f1"/></svg>
  <div class="brand"><span class="brand-mark"></span>Corvixo</div>
  <div class="cover-band"><div class="kicker">WELCOME TO</div><div class="name">CORVIXO</div></div>
</section>

<!-- Slide 2: Timeline -->
<section class="slide" style="top:724px">
  <svg class="swoosh" viewBox="0 0 1096 617" aria-hidden="true"><path d="M380 0 C 700 20, 960 70, 1096 190 L1096 0 Z" fill="#f1f1f1"/></svg>
  <div class="title-tab"></div>
  <h2 class="slide-title" style="left:40px">TIMELINE</h2>
  <div class="brand"><span class="brand-mark"></span>Corvixo</div>
  <svg style="left:0;top:0" width="1096" height="617" viewBox="0 0 1096 617" aria-hidden="true">
    <path d="M0 147 H911 A136.5 136.5 0 0 1 911 420 H0" fill="none" stroke="#111" stroke-width="32"/>
    <path d="M0 147 H911 A136.5 136.5 0 0 1 911 420 H0" fill="none" stroke="#fff" stroke-width="2" stroke-dasharray="10 9"/>
    <g fill="#f7b887"><circle cx="123" cy="147" r="46"/><circle cx="405" cy="147" r="46"/><circle cx="687" cy="147" r="46"/><circle cx="266" cy="420" r="46"/><circle cx="548" cy="420" r="46"/><circle cx="830" cy="420" r="46"/></g>
    <g fill="#ee7623"><circle cx="123" cy="147" r="36"/><circle cx="405" cy="147" r="36"/><circle cx="687" cy="147" r="36"/><circle cx="266" cy="420" r="36"/><circle cx="548" cy="420" r="36"/><circle cx="830" cy="420" r="36"/></g>
    <g fill="none" stroke="#fff" stroke-width="2" stroke-linecap="round" stroke-linejoin="round">
      <path d="M108 140 h8 l14 -8 v28 l-14 -8 h-8 z M112 152 v8"/>
      <path d="M405 132 c6 6 6 16 0 24 c-6 -8 -6 -18 0 -24 z M393 162 h24"/>
      <circle cx="687" cy="140" r="8"/><path d="M673 162 c2 -9 26 -9 28 0 M679 140 v-4 c0 -10 16 -10 16 0 v4"/>
      <circle cx="263" cy="417" r="11"/><path d="M271 425 l9 9"/>
      <rect x="538" y="406" width="20" height="26" rx="2"/><path d="M543 414 h10 M543 420 h10"/>
      <rect x="818" y="416" width="12" height="14"/><path d="M832 422 l8 -10 c3 -3 6 0 4 3 l-2 5 h6 v8 h-16"/>
    </g>
  </svg>
  <div class="milestone" style="left:123px;top:200px"><div class="year">1995</div><p>lorem ipsum dolor sit<br>amet, consectetuer<br>adipiscing elit.</p></div>
  <div class="milestone" style="left:405px;top:200px"><div class="year">2000</div><p>lorem ipsum dolor sit<br>amet, consectetuer<br>adipiscing elit.</p></div>
  <div class="milestone" style="left:687px;top:200px"><div class="year">2005</div><p>lorem ipsum dolor sit<br>amet, consectetuer<br>adipiscing elit.</p></div>
  <div class="milestone" style="left:266px;top:474px"><div class="year">2010</div><p>lorem ipsum dolor sit<br>amet, consectetuer<br>adipiscing elit.</p></div>
  <div class="milestone" style="left:548px;top:474px"><div class="year">2015</div><p>lorem ipsum dolor sit<br>amet, consectetuer<br>adipiscing elit.</p></div>
  <div class="milestone" style="left:830px;top:474px"><div class="year">2020</div><p>lorem ipsum dolor sit<br>amet, consectetuer<br>adipiscing elit.</p></div>
  <div class="page-no">2</div>
</section>

<!-- Slide 3: Services -->
<section class="slide" style="top:1405px">
  <svg class="swoosh" viewBox="0 0 1096 617" aria-hidden="true"><path d="M380 0 C 700 20, 960 70, 1096 190 L1096 0 Z" fill="#f1f1f1"/></svg>
  <div class="title-tab"></div>
  <h2 class="slide-title">OUR SERVICES</h2>
  <div class="brand"><span class="brand-mark"></span>Corvixo</div>
  <svg style="left:0;top:0" width="1096" height="617" viewBox="0 0 1096 617" aria-hidden="true">
    <defs><path id="tag" d="M0 0 H70 L100 32 L70 64 H0 Z" fill="#ee7623"/></defs>
    <use href="#tag" x="55" y="160"/><use href="#tag" x="55" y="284"/><use href="#tag" x="55" y="407"/>
    <use href="#tag" x="593" y="160"/><use href="#tag" x="593" y="284"/><use href="#tag" x="593" y="407"/>
    <g fill="none" stroke="#fff" stroke-width="2.2" stroke-linecap="round" stroke-linejoin="round">
      <rect x="80" y="180" width="26" height="20" rx="2"/><path d="M86 188 h10 M86 194 h6"/><path d="M104 196 l4 4 l7 -8"/>
      <rect x="80" y="304" width="28" height="20" rx="2"/><path d="M80 311 h28 M85 319 h8"/>
      <rect x="84" y="425" width="22" height="30" rx="3"/><circle cx="95" cy="440" r="6"/>
      <path d="M618 204 h32 M622 200 v-8 M630 200 v-12 M638 200 v-8 M646 200 v-16 M620 186 l10 -6 l8 4 l10 -8"/>
      <circle cx="632" cy="316" r="13"/><path d="M632 303 v13 h13"/>
      <circle cx="630" cy="439" r="9"/><path d="M630 424 v6 M630 448 v6 M615 439 h6 M639 439 h6 M645 428 h6 M645 450 h6"/>
    </g>
  </svg>
  <div class="service" style="left:175px;top:158px"><h3>Core HR and Payroll</h3><p>Integrate disparate employment data in a single<br>human resource information system (HRIS).</p></div>
  <div class="service" style="left:175px;top:284px"><h3>Recruiting and Onboarding</h3><p>Our recruiting solutions can help you conduct<br>talent acquisition and improve the onboarding<br>experience.</p></div>
  <div class="service" style="left:175px;top:408px"><h3>Learning and Development</h3><p>Deliver personalized cognitive coaching and<br>microlearning by taking advantage of analytics and<br>succession planning.</p></div>
  <div class="service" style="left:710px;top:158px"><h3>Performance and Compensation</h3><p>Improve employee performance management and<br>keep your entire workforce satisfied and motivated.</p></div>
  <div class="service" style="left:710px;top:284px"><h3>HR Analytics</h3><p>Make better decisions about hiring, diversity,<br>turnover, performance, and more.</p></div>
  <div class="service" style="left:710px;top:408px"><h3>Workplace Transformation</h3><p>Manage a diverse workforce and make the shift to<br>a more collaborative, team-based work<br>environment.</p></div>
  <div class="footer"><span class="social"></span><span class="social"></span><span class="social"></span><span class="social"></span><span class="divider"></span>© Copyrights 2023 Company name | All Rights Reserved</div>
  <div class="page-no">3</div>
</section>

<!-- Slide 4: Features chart -->
<section class="slide" style="top:2086px">
  <svg class="swoosh" viewBox="0 0 1096 617" aria-hidden="true"><path d="M380 0 C 700 20, 960 70, 1096 190 L1096 0 Z" fill="#f1f1f1"/></svg>
  <div class="title-tab"></div>
  <h2 class="slide-title">LATEST FEATURES</h2>
  <div class="brand"><span class="brand-mark"></span>Corvixo</div>
  <svg style="left:0;top:0" width="1096" height="617" viewBox="0 0 1096 617" font-family="Roboto, sans-serif" font-size="11" aria-label="Bar chart comparing two series from Sunday to Saturday">
    <g stroke="#e3e3e3" stroke-width="1">
      <path d="M127 141 H665 M127 196 H665 M127 252 H665 M127 307 H665 M127 362 H665 M127 418 H665"/>
      <path d="M127 141 V473 M204 141 V473 M281 141 V473 M358 141 V473 M434 141 V473 M511 141 V473 M588 141 V473 M665 141 V473"/>
    </g>
    <path d="M127 473 H665" stroke="#999"/>
    <g fill="#111" text-anchor="end"><text x="120" y="145">120</text><text x="120" y="200">100</text><text x="120" y="256">80</text><text x="120" y="311">60</text><text x="120" y="366">40</text><text x="120" y="422">20</text><text x="120" y="477">0</text></g>
    <g fill="#111">
      <rect x="151" y="196" width="14" height="277"/><rect x="228" y="224" width="14" height="249"/><rect x="305" y="335" width="14" height="138"/>
      <rect x="382" y="196" width="14" height="277"/><rect x="458" y="196" width="14" height="277"/><rect x="535" y="307" width="14" height="166"/><rect x="612" y="335" width="14" height="138"/>
    </g>
    <g fill="#ee7623">
      <rect x="170" y="224" width="14" height="249"/><rect x="247" y="252" width="14" height="221"/><rect x="324" y="196" width="14" height="277"/>
      <rect x="401" y="307" width="14" height="166"/><rect x="477" y="224" width="14" height="249"/><rect x="554" y="265" width="14" height="208"/><rect x="631" y="196" width="14" height="277"/>
    </g>
    <g fill="#111" font-weight="700" font-size="11" text-anchor="middle">
      <text x="158" y="190">100</text><text x="177" y="218">90</text><text x="235" y="218">90</text><text x="254" y="246">80</text>
      <text x="312" y="329">50</text><text x="331" y="190">100</text><text x="389" y="190">100</text><text x="408" y="301">60</text>
      <text x="465" y="190">100</text><text x="484" y="218">90</text><text x="542" y="301">60</text><text x="561" y="259">75</text>
      <text x="619" y="329">50</text><text x="638" y="190">100</text>
      <text x="167" y="493">Sun</text><text x="244" y="493">Mon</text><text x="321" y="493">Tue</text><text x="398" y="493">Wed</text><text x="474" y="493">Thu</text><text x="551" y="493">Fri</text><text x="628" y="493">Sat</text>
    </g>
  </svg>
  <div class="feature" style="top:132px"><h4>Feature One</h4><p>Lorem ipsum dolor sit consectetur adipiscing<br>elit, sed do eiusmod tempor</p></div>
  <div class="feature" style="top:240px"><h4>Feature Two</h4><p>Lorem ipsum dolor sit consectetur adipiscing<br>elit, sed do eiusmod</p></div>
  <div class="feature" style="top:341px"><h4>Feature Three</h4><p>Lorem ipsum dolor sit consectetur adipiscing<br>elit, sed do eiusmod tempor</p></div>
  <div class="feature" style="top:443px"><h4>Feature Four</h4><p>Lorem ipsum dolor sit consectetur adipiscing<br>elit, sed do eiusmod</p></div>
  <div class="footer"><span class="social"></span><span class="social"></span><span class="social"></span><span class="social"></span><span class="divider"></span>© Copyrights 2023 Company name | All Rights Reserved</div>
  <div class="page-no">4</div>
</section>

<!-- Slide 5: Team -->
<section class="slide" style="top:2765px">
  <svg class="swoosh" viewBox="0 0 1096 617" aria-hidden="true"><path d="M380 0 C 700 20, 960 70, 1096 190 L1096 0 Z" fill="#f1f1f1"/></svg>
  <div class="title-tab"></div>
  <h2 class="slide-title">OUR TEAM</h2>
  <div class="brand"><span class="brand-mark"></span>Corvixo</div>
  <div class="member" style="left:218px;top:175px"><div class="portrait" role="img" aria-label="Portrait photo of the CEO"></div><h5>John Doe</h5><div class="role">CEO</div><p>Lorem ipsum dolor sit amet, cons<br>ectetuer adipiscing elit. Maecenas<br>porttitor congue massa. Fusce posu<br>ere, magna sed pulvina</p></div>
  <div class="member" style="left:554px;top:175px"><div class="portrait" role="img" aria-label="Portrait photo of the support manager"></div><h5>Milan</h5><div class="role">Support Manager</div><p>Lorem ipsum dolor sit amet, cons<br>ectetuer adipiscing elit. Maecenas<br>porttitor congue massa. Fusce posu<br>ere, magna sed pulvina</p></div>
  <div class="member" style="left:889px;top:175px"><div class="portrait" role="img" aria-label="Portrait photo of the business head"></div><h5>Owen Hale</h5><div class="role">Business Head</div><p>Lorem ipsum dolor sit amet, cons<br>ectetuer adipiscing elit. Maecenas<br>porttitor congue massa. Fusce posu<br>ere, magna sed pulvina</p></div>
  <div class="footer"><span class="social"></span><span class="social"></span><span class="social"></span><span class="social"></span><span class="divider"></span>© Copyrights 2023 Company name | All Rights Reserved</div>
  <div class="page-no">5</div>
</section>

<!-- Slide 6: Thank you -->
<section class="slide" style="top:3446px">
  <div class="thanks-band"></div>
  <h2 class="thanks-title">THANK YOU</h2>
  <div class="brand"><span class="brand-mark"></span>Corvixo</div>
  <div class="thanks-photo" role="img" aria-label="Photo of a business team meeting around a table with laptops"></div>
  <div class="footer"><span class="social"></span><span class="social"></span><span class="social"></span><span class="social"></span><span class="divider"></span>© Copyrights 2023 Company name | All Rights Reserved</div>
  <div class="page-no">6</div>
</section>

</body>
</html>
```